Redesign Business Cards, Attached

Please read instructions carefully. If you have any questions send a message before submitting your ONE design. Please redesign attached business cards. Double sided. Use same content and descriptions. Use black, silver, crimson red and gold colors. My only issue with the attached design is the background colors. I like the layout as-is. I can provide the individual pictures on the back side later. Do not submit more than one design. One submission shall include both front and back. Do not submit front and back separately. A second project will be launched to create a matching post card after completion of this.
Industry/Entity Type
see description and attachments.
Contact Information for Business Card
Requirements
Must have
- see description and attachments.
Nice to have
Should not have

```html
<!DOCTYPE html>
<html lang="en">
<head>
<meta charset="utf-8">
<title>Harbor Helm's Business Cards</title>
<link href="https://fonts.googleapis.com/css2?family=Montserrat:wght@400;700&family=Delius&display=swap" rel="stylesheet">
<style>
  :root {
    --crimson: #9b0a0f;
    --crimson-dark: #7a080c;
    --black: #111111;
    --white: #ffffff;
    --sea-light: #b7c3cf;
    --sea-mid: #7f8e9e;
    --sea-dark: #4a5563;
    --page: #e9e7e3;
    --ink: #1a1a1a;
  }
  * { margin: 0; padding: 0; box-sizing: border-box; }
  html, body { width: 1200px; height: 975px; overflow: hidden; }
  body {
    background: var(--page);
    position: relative;
    font-family: "Montserrat", sans-serif;
  }
  .card {
    position: absolute;
    left: 240px;
    width: 720px;
    height: 411px;
    background: var(--white);
    overflow: hidden;
    box-shadow: 0 6px 18px rgba(0,0,0,.18);
  }
  .card--front { top: 51px; }
  .card--back { top: 513px; }
  .card svg.shapes { position: absolute; inset: 0; }

  /* front */
  .brand {
    position: absolute;
    left: 40px; top: 48px;
    display: flex; align-items: center; gap: 12px;
    color: var(--white);
    font-weight: 700; font-size: 22px; line-height: 1.15;
  }
  .brand__dot {
    width: 30px; height: 30px; border-radius: 50%;
    background: var(--white);
  }
  .contact {
    position: absolute;
    left: 420px; top: 222px;
    color: var(--white);
    font-size: 17px; line-height: 1.45;
  }
  .contact__name { font-weight: 700; font-size: 25px; letter-spacing: .5px; margin-bottom: 4px; }

  /* back */
  .service {
    position: absolute;
    width: 128px; height: 56px;
    display: flex; align-items: center; justify-content: center;
    text-align: center;
    font-family: "Delius", cursive;
    font-size: 14px; line-height: 1.05;
    padding: 4px;
  }
  .service--red { background: var(--crimson); color: var(--white); }
  .service--white { background: var(--white); color: var(--ink); }
  .website {
    position: absolute;
    left: 0; right: 110px; top: 300px;
    text-align: center;
    font-weight: 700; font-size: 24px;
    color: var(--ink);
    letter-spacing: .3px;
  }
</style>
</head>
<body>

<section class="card card--front" aria-label="Business card front">
  <svg class="shapes" width="720" height="411" viewBox="0 0 720 411">
    <defs>
      <linearGradient id="seaFront" x1="0" y1="0" x2="1" y2="1">
        <stop offset="0" stop-color="var(--sea-mid)"/>
        <stop offset=".5" stop-color="var(--sea-light)"/>
        <stop offset="1" stop-color="var(--sea-dark)"/>
      </linearGradient>
    </defs>
    <rect width="720" height="411" fill="url(#seaFront)" role="img" aria-label="Photo of a motor boat cruising on open water"/>
    <polygon points="300,411 355,170 720,130 720,411" fill="var(--white)"/>
    <polygon points="330,411 382,186 720,150 720,411" fill="var(--black)"/>
    <polygon points="350,411 400,202 720,170 720,411" fill="var(--crimson)"/>
  </svg>
  <div class="brand">
    <span class="brand__dot"></span>
    <span>Harbor Helm's<br>Boat Training &amp; Charters</span>
  </div>
  <div class="contact">
    <p class="contact__name">DANA R. WHITLOW</p>
    <p>USCG Licensed Captain</p>
    <p>Certified Instructor</p>
    <p>(555) 014-2287</p>
    <p>service@hireahelmsman.com</p>
    <p>www.HireAHelmsman.com</p>
  </div>
</section>

<section class="card card--back" aria-label="Business card back">
  <svg class="shapes" width="720" height="411" viewBox="0 0 720 411">
    <defs>
      <linearGradient id="seaBack" x1="0" y1="0" x2="1" y2="1">
        <stop offset="0" stop-color="var(--sea-dark)"/>
        <stop offset=".55" stop-color="var(--sea-light)"/>
        <stop offset="1" stop-color="var(--sea-mid)"/>
      </linearGradient>
      <linearGradient id="crimsonPanel" x1="0" y1="0" x2="1" y2="1">
        <stop offset="0" stop-color="var(--crimson-dark)"/>
        <stop offset="1" stop-color="var(--crimson)"/>
      </linearGradient>
    </defs>
    <polygon points="0,0 400,0 330,175 0,200" fill="url(#crimsonPanel)"/>
    <polygon points="400,0 720,0 720,411 560,411 320,175" fill="url(#seaBack)" role="img" aria-label="Photo of a motor boat cutting a wake through the sea"/>
  </svg>

  <div class="service service--white" style="left:110px;top:148px">Hands-On Boat Training</div>
  <div class="service service--red" style="left:250px;top:148px">Introduction to Power boating</div>
  <div class="service service--white" style="left:390px;top:160px">Precision Docking &amp; Boat Handling</div>
  <div class="service service--red" style="left:530px;top:172px">Open Water Boat Handling</div>

  <div class="service service--red" style="left:60px;top:204px">Island Anchoring</div>
  <div class="service service--white" style="left:200px;top:210px">Open Water Advanced Maneuvers</div>
  <div class="service service--red" style="left:340px;top:222px">Coastal Navigation</div>
  <div class="service service--white" style="left:480px;top:234px">Captaining/ Piloting Service for Your Outings</div>

  <p class="website">www.HireAHelmsman.com</p>
</section>

</body>
</html>
```